KORPIX POSTCARD

I submitted my postcard and printer said it is not acceptable here are the comments
Item 948762 - Front file: Uploaded png is 3.3 x 2.2" at 300 dpi. Back file: Uploaded png is 5 x 3.3" at 200 dpi. There is text and images too close to the edges for the front and back. Both front/back files are low resolution and have poor print quality. The correct size for a jumbo postcard is 8.75 x 5.75". The intended bleed extends to the edges and all important text and/or elements are to remain at least 3/8" away from the edges. Try saving as a PDF from the source file at the correct size for a possible better printing output.

Item 948763 - Front file: Uploaded jpg is 7 x 5" at 200 dpi. Back file: Uploaded jpg is 8 x 5" at 220 dpi. Both front/back files are low resolution and have poor print quality. The correct size for a Medium TLRS card is 8.25 x 6.75" The intended bleed extends to the edges of the canvas and all important text and/or elements are to remain at least 3/8" away from the edges. Try saving as a PDF from the source file at the correct size for a possible better printing output.

```html
<!DOCTYPE html>
<html lang="en">
<head>
<meta charset="utf-8">
<title>Korpix Postcard</title>
<link href="https://fonts.googleapis.com/css2?family=Montserrat:wght@500;700;800;900&family=Open+Sans:wght@400;600;700&display=swap" rel="stylesheet">
<style>
:root{
  --blue:#1c5fbf;
  --blue-light:#3f86e0;
  --navy:#0c2d6b;
  --yellow:#f7c726;
  --red:#d3252c;
  --white:#ffffff;
  --paper:#eef3fa;
  --ink:#1b2a44;
  --grey:#d9e1ec;
}
*{box-sizing:border-box;margin:0;padding:0}
html,body{width:887px;height:1200px;overflow:hidden;background:#fff;font-family:"Open Sans",Arial,sans-serif;color:var(--ink)}
.card{position:absolute;left:10px;width:867px;overflow:hidden;background:var(--white);box-shadow:0 0 0 1px #cfd8e6}
.front{top:12px;height:570px}
.back{top:618px;height:568px}
.abs{position:absolute}
.heading{font-family:"Montserrat",Arial,sans-serif}

/* front */
.brand{left:34px;top:22px;display:flex;align-items:center;gap:10px}
.brand-dot{width:34px;height:34px;border-radius:50%;background:var(--blue)}
.brand-name{font-family:"Montserrat",Arial,sans-serif;font-weight:800;font-size:42px;color:var(--navy);letter-spacing:1px}
.team-photo{right:0;top:0;width:460px;height:305px;background:linear-gradient(160deg,#dbe8f7 0%,#b9cfe9 55%,#8fb0da 100%)}
.hero-text{left:34px;top:112px;color:var(--white)}
.hero-text .kicker{font-weight:800;font-size:38px;letter-spacing:1px;line-height:1}
.hero-text .main{font-weight:900;font-size:58px;line-height:1.05;color:var(--white)}
.hero-street{left:34px;top:246px;background:var(--navy);color:var(--yellow);font-family:"Montserrat",Arial,sans-serif;font-weight:800;font-size:22px;padding:6px 14px;letter-spacing:1px}
.badge{left:432px;top:168px;width:120px;height:120px;border-radius:50%;background:var(--red);border:4px solid var(--white);color:var(--white);text-align:center;display:flex;flex-direction:column;justify-content:center;font-family:"Montserrat",Arial,sans-serif;font-weight:700;font-size:11px;line-height:1.2}
.badge strong{font-size:14px;font-weight:900;color:var(--yellow)}
.features{left:34px;top:322px;width:520px;display:grid;grid-template-columns:1fr 1fr;gap:14px 22px}
.feature{display:flex;gap:8px;font-size:12.5px;line-height:1.35;color:var(--ink)}
.feature svg{flex:none;margin-top:2px}
.specialists{left:582px;top:300px;width:285px;height:128px;background:var(--blue);color:var(--white);padding:12px 16px}
.specialists h3{font-family:"Montserrat",Arial,sans-serif;font-weight:800;font-size:15px;line-height:1.15;color:var(--yellow)}
.specialists ul{list-style:none;display:grid;grid-template-columns:1fr 1fr;gap:3px 10px;margin-top:8px;font-size:11.5px}
.specialists li::before{content:"\2022 ";color:var(--yellow)}
.phone-box{left:582px;top:430px;width:285px;height:48px;background:var(--navy);display:flex;align-items:center;justify-content:center;gap:10px;color:var(--white);font-family:"Montserrat",Arial,sans-serif;font-weight:800;font-size:28px}
.partners{left:0;top:488px;width:867px;height:82px;background:var(--paper);display:flex;align-items:center;justify-content:space-around;padding:0 20px}
.partner{width:66px;height:30px;border-radius:6px;background:var(--grey)}

/* back */
.doctor-photo{left:34px;top:28px;width:128px;height:128px;border-radius:50%;background:linear-gradient(180deg,#c9d8ec,#8ea9cf);border:4px solid var(--blue)}
.intro{left:184px;top:40px}
.intro .lang{font-family:"Montserrat",Arial,sans-serif;font-weight:800;font-size:28px;color:var(--navy)}
.intro .tele{font-weight:700;font-size:14px;color:var(--blue);letter-spacing:1px}
.intro .name{margin-top:22px;font-family:"Montserrat",Arial,sans-serif;font-weight:700;font-size:17px;color:var(--red)}
.indicia{right:30px;top:20px;width:118px;height:76px;border:1.5px solid var(--ink);font-size:9.5px;line-height:1.3;text-align:center;padding-top:8px;font-weight:600}
.mailing{left:560px;top:136px;font-family:"Montserrat",Arial,sans-serif;font-weight:700;font-size:16px;line-height:1.35;color:var(--ink)}
.mailing .to{font-size:12px;font-weight:600;margin-top:6px;color:#44536d}
.blue-field{left:0;top:222px;width:867px;height:346px;background:linear-gradient(135deg,var(--blue) 0%,var(--navy) 100%)}
.story{left:34px;top:240px;width:430px;color:var(--white)}
.story h2{font-family:"Montserrat",Arial,sans-serif;font-weight:800;font-size:26px;line-height:1.1}
.story h2 span{display:block;color:var(--yellow);font-size:22px}
.story p{font-size:11.5px;line-height:1.45;margin-top:10px}
.back-phone{left:34px;top:452px;color:var(--white);font-family:"Montserrat",Arial,sans-serif;font-weight:900;font-size:46px}
.web-bar{left:0;top:522px;width:867px;height:46px;background:var(--yellow);color:var(--navy);font-family:"Montserrat",Arial,sans-serif;font-weight:800;font-size:24px;display:flex;align-items:center;padding-left:110px;letter-spacing:1px}
.services{left:492px;top:240px;width:350px;height:268px;background:var(--white);border-radius:8px;padding:16px 18px}
.services h3{font-family:"Montserrat",Arial,sans-serif;font-weight:800;font-size:16px;color:var(--navy)}
.services ul{list-style:none;display:grid;grid-template-columns:1fr 1fr;gap:9px 14px;margin-top:14px;font-size:12px}
.services li{display:flex;gap:6px;align-items:flex-start;line-height:1.25}
.services li svg{flex:none;margin-top:1px}
</style>
</head>
<body>

<section class="card front">
  <div class="abs team-photo" role="img" aria-label="Photo of a smiling team of doctors and nurses in white coats and scrubs"></div>
  <svg class="abs" style="left:0;top:0" width="867" height="570" aria-hidden="true">
    <path d="M0 92 L470 92 L440 305 L0 305 Z" fill="var(--blue)"/>
  </svg>

  <div class="abs brand"><span class="brand-dot"></span><span class="brand-name">KORPIX</span></div>

  <div class="abs hero-text heading">
    <div class="kicker">PRIMARY CARE</div>
    <div class="main">MEDICINE</div>
  </div>
  <div class="abs hero-street">RIGHT ON HARBOR AVE</div>

  <div class="abs badge">All insurances<br>accepted<br>including<br><strong>MEDICARE<br>MEDICAID</strong></div>

  <div class="abs features">
    <div class="feature"><svg width="14" height="14" viewBox="0 0 14 14"><circle cx="7" cy="7" r="7" fill="var(--blue)"/><path d="M3.5 7.2l2.3 2.2 4.6-4.8" stroke="#fff" stroke-width="1.8" fill="none"/></svg><span>Clean, modern state of the art offices</span></div>
    <div class="feature"><svg width="14" height="14" viewBox="0 0 14 14"><circle cx="7" cy="7" r="7" fill="var(--blue)"/><path d="M3.5 7.2l2.3 2.2 4.6-4.8" stroke="#fff" stroke-width="1.8" fill="none"/></svg><span>Be seen by board certified internal medicine doctors</span></div>
    <div class="feature"><svg width="14" height="14" viewBox="0 0 14 14"><circle cx="7" cy="7" r="7" fill="var(--blue)"/><path d="M3.5 7.2l2.3 2.2 4.6-4.8" stroke="#fff" stroke-width="1.8" fill="none"/></svg><span>Accepting new patients, immediate appointments available</span></div>
    <div class="feature"><svg width="14" height="14" viewBox="0 0 14 14"><circle cx="7" cy="7" r="7" fill="var(--blue)"/><path d="M3.5 7.2l2.3 2.2 4.6-4.8" stroke="#fff" stroke-width="1.8" fill="none"/></svg><span>Every specialist you need, no shuffling between offices</span></div>
    <div class="feature"><svg width="14" height="14" viewBox="0 0 14 14"><circle cx="7" cy="7" r="7" fill="var(--blue)"/><path d="M3.5 7.2l2.3 2.2 4.6-4.8" stroke="#fff" stroke-width="1.8" fill="none"/></svg><span>On-site lab testing</span></div>
  </div>

  <div class="abs specialists">
    <h3>MULTIPLE SPECIALISTS<br>UNDER ONE ROOF</h3>
    <ul>
      <li>Psychiatry</li><li>Cardiology</li>
      <li>Podiatry</li><li>Pain Care</li>
      <li>Pulmonology</li><li>Endocrinology</li>
    </ul>
  </div>

  <div class="abs phone-box">
    <svg width="26" height="26" viewBox="0 0 24 24" aria-hidden="true"><path d="M6.6 10.8a15 15 0 0 0 6.6 6.6l2.2-2.2c.3-.3.7-.4 1-.2 1.1.4 2.3.6 3.6.6.6 0 1 .4 1 1V20c0 .6-.4 1-1 1A17 17 0 0 1 3 4c0-.6.4-1 1-1h3.5c.6 0 1 .4 1 1 0 1.3.2 2.5.6 3.6.1.3 0 .7-.2 1z" fill="var(--yellow)"/></svg>
    555-014-2280
  </div>

  <div class="abs partners">
    <span class="partner"></span><span class="partner"></span><span class="partner"></span><span class="partner"></span><span class="partner"></span><span class="partner"></span><span class="partner"></span><span class="partner"></span><span class="partner"></span><span class="partner"></span>
  </div>
</section>

<section class="card back">
  <div class="abs doctor-photo" role="img" aria-label="Portrait photo of the doctor"></div>
  <div class="abs intro">
    <div class="lang">SE HABLA ESPAÑOL</div>
    <div class="tele">TELE-VISITS AVAILABLE</div>
    <div class="name">LENA MORVATH, MD</div>
  </div>
  <div class="abs indicia">PRSRT STD<br>ECRWSS<br>U.S. POSTAGE PAID<br>TLRS RETAIL</div>
  <div class="abs mailing">418 HARBOR AVENUE<br>LINDEN, NJ 07099<div class="to">LOCAL POSTAL CUSTOMER</div></div>

  <div class="abs blue-field"></div>
  <div class="abs story">
    <h2>A Doctor Who Cares<span>Experience You Can Trust</span></h2>
    <p>Dr. Morvath has been practicing medicine in Linden for over 12 years.</p>
    <p>She previously ran a primary care practice with Riverside General Hospital for 10 years. Dr. Morvath has grown alongside the community and has seen the changes in health care first hand. Her practice offers you the care you deserve.</p>
    <p>Dr. Morvath prides herself on giving every patient the time and attention they need and holds privileges at Riverside General.</p>
  </div>
  <div class="abs back-phone">555-014-2280</div>
  <div class="abs web-bar">www.korpix.ie</div>

  <div class="abs services">
    <h3>All Primary Care Services Including:</h3>
    <ul>
      <li><svg width="12" height="12" viewBox="0 0 14 14"><path d="M2 7.5l3 3 7-7.5" stroke="var(--blue)" stroke-width="2.4" fill="none"/></svg>Hypertension</li>
      <li><svg width="12" height="12" viewBox="0 0 14 14"><path d="M2 7.5l3 3 7-7.5" stroke="var(--blue)" stroke-width="2.4" fill="none"/></svg>Acute Accidents</li>
      <li><svg width="12" height="12" viewBox="0 0 14 14"><path d="M2 7.5l3 3 7-7.5" stroke="var(--blue)" stroke-width="2.4" fill="none"/></svg>Diabetes</li>
      <li><svg width="12" height="12" viewBox="0 0 14 14"><path d="M2 7.5l3 3 7-7.5" stroke="var(--blue)" stroke-width="2.4" fill="none"/></svg>Blood Tests &amp; Labs</li>
      <li><svg width="12" height="12" viewBox="0 0 14 14"><path d="M2 7.5l3 3 7-7.5" stroke="var(--blue)" stroke-width="2.4" fill="none"/></svg>Cholesterol</li>
      <li><svg width="12" height="12" viewBox="0 0 14 14"><path d="M2 7.5l3 3 7-7.5" stroke="var(--blue)" stroke-width="2.4" fill="none"/></svg>Vaccinations</li>
      <li><svg width="12" height="12" viewBox="0 0 14 14"><path d="M2 7.5l3 3 7-7.5" stroke="var(--blue)" stroke-width="2.4" fill="none"/></svg>Asthma &amp; COPD</li>
      <li><svg width="12" height="12" viewBox="0 0 14 14"><path d="M2 7.5l3 3 7-7.5" stroke="var(--blue)" stroke-width="2.4" fill="none"/></svg>Flu Shots</li>
      <li><svg width="12" height="12" viewBox="0 0 14 14"><path d="M2 7.5l3 3 7-7.5" stroke="var(--blue)" stroke-width="2.4" fill="none"/></svg>Thyroid Care</li>
      <li><svg width="12" height="12" viewBox="0 0 14 14"><path d="M2 7.5l3 3 7-7.5" stroke="var(--blue)" stroke-width="2.4" fill="none"/></svg>Physical Exams</li>
      <li><svg width="12" height="12" viewBox="0 0 14 14"><path d="M2 7.5l3 3 7-7.5" stroke="var(--blue)" stroke-width="2.4" fill="none"/></svg>Sports Physicals</li>
      <li><svg width="12" height="12" viewBox="0 0 14 14"><path d="M2 7.5l3 3 7-7.5" stroke="var(--blue)" stroke-width="2.4" fill="none"/></svg>Women's Health</li>
    </ul>
  </div>
</section>

</body>
</html>
```